Iron Ridge Roofing Business Card

Need a business card with the logo that was designed here

Contact Information for Business Card

Name, Title, Phone, Email, Website, Company name

```html
<!DOCTYPE html>
<html lang="en">
<head>
<meta charset="utf-8">
<title>Iron Ridge Roofing – Business Card</title>
<link rel="stylesheet" href="https://fonts.googleapis.com/css2?family=Montserrat:wght@400;700&display=swap">
<style>
  :root {
    --backdrop: #d4d8d9;
    --paper: #f8f8f6;
    --brand-blue: #1d3c9a;
    --ink-grey: #5a5a5a;
    --edge-blue: #1a3597;
  }
  * { box-sizing: border-box; margin: 0; padding: 0; }
  html, body { width: 1200px; height: 829px; overflow: hidden; }
  body {
    background: var(--backdrop);
    font-family: "Montserrat", sans-serif;
    position: relative;
  }
  .card {
    position: absolute;
    top: 264px;
    width: 520px;
    height: 300px;
    background: var(--paper);
    border-bottom: 4px solid var(--edge-blue);
    box-shadow: 0 6px 18px rgba(0,0,0,0.12);
  }
  .card--front { left: 50px; }
  .card--back { left: 630px; display: flex; align-items: center; justify-content: center; }

  .brand-name {
    font-family: "Montserrat", sans-serif;
    font-weight: 700;
    color: var(--brand-blue);
    letter-spacing: 0.04em;
  }
  .card--front .brand-name {
    position: absolute;
    left: 64px;
    top: 34px;
    font-size: 18px;
  }
  .card--back .brand-name { font-size: 38px; text-align: center; line-height: 1.15; }

  .accent-bar {
    position: absolute;
    left: 36px;
    top: 84px;
    width: 10px;
    height: 26px;
    background: var(--brand-blue);
  }
  .contact {
    position: absolute;
    left: 64px;
    top: 84px;
    color: var(--ink-grey);
  }
  .contact__name {
    font-weight: 700;
    font-size: 19px;
    color: var(--brand-blue);
    letter-spacing: 0.06em;
    line-height: 1.1;
  }
  .contact__title { font-size: 13px; margin-top: 2px; }
  .contact__address { font-size: 13px; margin-top: 12px; line-height: 1.45; }
  .contact__list { list-style: none; margin-top: 12px; font-size: 13px; line-height: 1.55; }
  .contact__list li { display: flex; align-items: center; gap: 8px; }
  .contact__list svg { width: 10px; height: 10px; fill: var(--brand-blue); flex: none; }
</style>
</head>
<body>
  <section class="card card--front">
    <div class="brand-name">IRON RIDGE ROOFING</div>
    <span class="accent-bar"></span>
    <div class="contact">
      <p class="contact__name">DERMOT HALLIS</p>
      <p class="contact__title">Managing Director</p>
      <p class="contact__address">418 W Fenwick Avenue<br>Marlow County Name 6120</p>
      <ul class="contact__list">
        <li>
          <svg viewBox="0 0 10 10" aria-hidden="true"><path d="M2 0.5 L3.8 2.4 L2.9 3.6 Q4 5.8 6.4 7.1 L7.6 6.2 L9.5 8 L8.3 9.5 Q1.5 8 0.5 1.7 Z"/></svg>
          0491 572 316
        </li>
        <li>
          <svg viewBox="0 0 10 10" aria-hidden="true"><path d="M0.5 2 H9.5 V8.5 H0.5 Z M1 2.5 L5 5.6 L9 2.5" stroke="#f8f8f6" stroke-width="0.8"/></svg>
          info@ironridgeroofing.com
        </li>
        <li>
          <svg viewBox="0 0 10 10" aria-hidden="true"><circle cx="5" cy="5" r="4.5"/><path d="M0.5 5 H9.5 M5 0.5 Q2.5 5 5 9.5 M5 0.5 Q7.5 5 5 9.5" stroke="#f8f8f6" stroke-width="0.7" fill="none"/></svg>
          www.ironridgeroofing.com
        </li>
      </ul>
    </div>
  </section>

  <section class="card card--back">
    <div class="brand-name">IRON RIDGE<br>ROOFING</div>
  </section>
</body>
</html>
```